We need an attractive business card design that is modern and inviting. We like the blue and yellow (or gold) colors that are displayed with the logo. The business should communicate trust, experience, and integrity.

Target Market(s)

Residential and Commercial

Industry/Entity Type

Business

Contact Information for Business Card

Recessed Lighting
LED Retro Fit
Sign Repair
Alarms and Cameras
Mobile Home Services
24hr service calls

Font styles to use
Serif
Sans Serif

Colors
3176b5
0455a3
fece3e
fbee3e

Requirements
Must have
• Brondle Electric
• Owner: Marcus Tivane
• Licensed and Insured
• TECL #58917
Nice to have
• Exquisite Detail!!
• Over 20 years of experience
Should not have
• Nothing boring or traditional!!!

```html
<!DOCTYPE html>
<html lang="en">
<head>
<meta charset="utf-8">
<title>Brondle Electric – Business Card</title>
<link rel="stylesheet" href="https://fonts.googleapis.com/css2?family=Open+Sans:wght@700&family=Questrial&display=swap">
<style>
  :root {
    --blue: #0f5aa8;
    --blue-deep: #0455a3;
    --blue-soft: #3176b5;
    --yellow: #f0e22a;
    --white: #ffffff;
    --paper: #f4f4f4;
    --ink: #3a3a3a;
    --stage: #3b3b3b;
  }
  * { box-sizing: border-box; margin: 0; padding: 0; }
  html, body { width: 1200px; height: 965px; overflow: hidden; background: var(--stage); }
  .canvas { position: relative; width: 1200px; height: 965px; font-family: "Questrial", sans-serif; }
  .card { position: absolute; left: 246px; width: 710px; height: 404px; border-radius: 34px; overflow: hidden; }
  .card--front { top: 60px; background: linear-gradient(180deg, var(--white), var(--paper)); }
  .card--back { top: 504px; background: var(--blue); }

  .brand-mark { position: absolute; border-radius: 50%; }
  .front-mark { left: 148px; top: 42px; width: 80px; height: 80px; border: 7px solid var(--blue-deep); }
  .front-wordmark { position: absolute; left: 34px; top: 118px; font-family: "Open Sans", sans-serif; font-weight: 700; font-size: 32px; letter-spacing: 1px; color: var(--blue-deep); white-space: nowrap; }

  .info-band { position: absolute; left: 0; top: 190px; width: 100%; height: 96px; background: linear-gradient(90deg, var(--blue) 0, var(--blue) 560px, var(--yellow) 560px); }
  .band-mark { left: 496px; top: 180px; width: 116px; height: 116px; background: var(--white); border: 10px solid var(--white); box-shadow: inset 0 0 0 7px var(--blue-deep); }
  .owner { position: absolute; left: 35px; top: 213px; color: var(--white); white-space: nowrap; }
  .owner-name { font-size: 23px; line-height: 26px; }
  .owner-role { font-size: 18px; line-height: 21px; }
  .license { position: absolute; left: 237px; top: 219px; color: var(--white); font-size: 18.5px; line-height: 21px; letter-spacing: 0.3px; white-space: nowrap; }

  .contact { position: absolute; left: 36px; top: 306px; color: var(--ink); font-size: 18px; line-height: 22px; white-space: nowrap; }
  .contact-row { display: flex; align-items: center; gap: 9px; }
  .contact-row svg { width: 15px; height: 15px; fill: var(--blue-deep); }
  .location { position: absolute; right: 42px; top: 305px; text-align: right; white-space: nowrap; }
  .location-name { color: var(--blue-deep); font-size: 20px; line-height: 24px; }
  .location-city { color: var(--ink); font-size: 18.5px; line-height: 21px; }
  .foot-band { position: absolute; left: 0; bottom: 0; width: 100%; height: 24px; background: linear-gradient(90deg, var(--blue) 0, var(--blue) 582px, var(--yellow) 582px); }

  .back-mark { left: 298px; top: 80px; width: 112px; height: 112px; border: 8px solid var(--white); }
  .back-wordmark { position: absolute; left: 0; top: 190px; width: 100%; text-align: center; font-family: "Open Sans", sans-serif; font-weight: 700; font-size: 44px; letter-spacing: 1.5px; color: var(--white); white-space: nowrap; }
  .services { position: absolute; left: 0; top: 278px; width: 100%; text-align: center; color: var(--white); font-size: 18px; line-height: 30px; white-space: nowrap; }
  .tagline { position: absolute; left: 0; bottom: 0; width: 100%; height: 30px; background: var(--yellow); color: var(--blue-deep); text-align: center; font-size: 19.5px; line-height: 30px; white-space: nowrap; }
</style>
</head>
<body>
<main class="canvas">
  <section class="card card--front">
    <div class="brand-mark front-mark"></div>
    <div class="front-wordmark">BRONDLE ELECTRIC</div>
    <div class="info-band"></div>
    <div class="brand-mark band-mark"></div>
    <div class="owner">
      <div class="owner-name">Marcus Tivane</div>
      <div class="owner-role">Owner</div>
    </div>
    <div class="license">
      <div>Licensed and Insured</div>
      <div>TECL #58917</div>
    </div>
    <div class="contact">
      <div class="contact-row">
        <svg viewBox="0 0 24 24"><path d="M6.6 10.8a15.1 15.1 0 0 0 6.6 6.6l2.2-2.2a1 1 0 0 1 1-.25 11.4 11.4 0 0 0 3.6.57 1 1 0 0 1 1 1V20a1 1 0 0 1-1 1A17 17 0 0 1 3 4a1 1 0 0 1 1-1h3.5a1 1 0 0 1 1 1c0 1.25.2 2.45.57 3.57a1 1 0 0 1-.25 1z"/></svg>
        <span>936-555-0182</span>
      </div>
      <div class="contact-row">
        <svg viewBox="0 0 24 24"><path d="M2 5h20v14H2z M3.5 6.5 12 13l8.5-6.5" stroke="#fff" stroke-width="1.6"/></svg>
        <span>info@brondleelectric.com</span>
      </div>
    </div>
    <div class="location">
      <div class="location-name">Brondle Electric :</div>
      <div class="location-city">Corvella,Texas</div>
    </div>
    <div class="foot-band"></div>
  </section>

  <section class="card card--back">
    <div class="brand-mark back-mark"></div>
    <div class="back-wordmark">BRONDLE ELECTRIC</div>
    <div class="services">
      <p>Residential and Commercial, Recessed Lighting, LED Retro Fit</p>
      <p>Sign Repair, Alarms and Cameras, Mobile Home Services, 24hr service calls</p>
    </div>
    <div class="tagline">Exquisite Detail!! Over 20 years of experience</div>
  </section>
</main>
</body>
</html>
```